Full service meeting planning company needs new business cards

Velmora Linkway is a full service meeting planning company that specializes in on-line conference registration web development and event communications. We combine citywide hotel management, mobile applications, eblast reminders, confirmation letters, and customized reporting to create a seamless registration process. We also manage group motor coach transportation, food and beverages, entertainment, stage and lighting for group of 10 to 4000.

Target Market(s)

Corporations and associations

Industry/Entity Type

Event Planning

Contact Information for Business Card

standard size 3.5" wide and 2" tall

Font styles to use
Serif
Sans Serif

Colors
f37122
f78f20
333333
5c5c5c
9d9d9d
f68d4d

Requirements
Must have
• {name}
• Velmora Linkway
• P.O. Box 7384, Grand Rapids, M I 49568
• www.velmoralinkway.com
• {email}
• {phone}
• {mobile phone}
Nice to have
• Our colors are black, grey and orange as an accent color
Should not have
• I am not happy with our website layout anymore either. It feels dark and old but it does explain who we are pretty well if you'd like to review; www.velmoralinkway.com

```html
<!DOCTYPE html>
<html lang="en">
<head>
<meta charset="utf-8">
<title>Velmora Linkway – Business Cards</title>
<link href="https://fonts.googleapis.com/css2?family=Jost:wght@400;500;600;700&display=swap" rel="stylesheet">
<style>
  :root {
    --orange: #f37122;
    --orange-warm: #f78f20;
    --charcoal: #333333;
    --ink: #2b2b2b;
    --grey: #5c5c5c;
    --grey-light: #9d9d9d;
    --paper: #ffffff;
    --stage: #2a2a2a;
  }
  * { margin: 0; padding: 0; box-sizing: border-box; }
  html, body { width: 1200px; height: 900px; overflow: hidden; }
  body {
    background: var(--stage);
    font-family: "Jost", "Helvetica Neue", Arial, sans-serif;
    position: relative;
  }
  .card {
    position: absolute;
    left: 270px;
    width: 660px;
    height: 377px;
    border-radius: 22px;
    overflow: hidden;
  }
  .card-back { top: 50px; background: var(--charcoal); }
  .card-front { top: 473px; background: var(--paper); }

  .back-name {
    position: absolute;
    left: 0; right: 0; top: 150px;
    text-align: center;
    color: var(--orange-warm);
    font-weight: 600;
    font-size: 46px;
    letter-spacing: 1px;
    text-transform: uppercase;
  }
  .back-web {
    position: absolute;
    right: 50px; bottom: 40px;
    color: var(--paper);
    font-size: 18px;
    letter-spacing: 0.5px;
  }
  .accent { color: var(--orange-warm); }

  .front-art { position: absolute; inset: 0; }
  .front-title {
    position: absolute;
    left: 38px; top: 98px;
    color: var(--ink);
    font-weight: 600;
    font-size: 31px;
    letter-spacing: 0.5px;
    text-transform: uppercase;
  }
  .person { position: absolute; left: 60px; top: 172px; }
  .person-name { color: var(--orange-warm); font-weight: 500; font-size: 25px; line-height: 1.1; }
  .person-role { color: var(--ink); font-size: 15px; margin-top: 2px; }
  .address {
    position: absolute;
    left: 78px; top: 262px;
    color: var(--grey);
    font-size: 16px;
    line-height: 1.3;
  }
  .contacts {
    position: absolute;
    right: 24px; top: 178px;
    list-style: none;
    color: var(--paper);
    font-size: 15.5px;
    line-height: 1.45;
  }
  .contacts li { display: flex; justify-content: flex-end; align-items: center; gap: 10px; }
  .contacts svg { width: 12px; height: 12px; flex: none; }
</style>
</head>
<body>

<section class="card card-back">
  <h1 class="back-name">Velmora Linkway</h1>
  <p class="back-web">www.<span class="accent">velmoralinkway</span>.com</p>
</section>

<section class="card card-front">
  <svg class="front-art" viewBox="0 0 660 377" aria-hidden="true">
    <rect x="440" y="92" width="220" height="8" fill="var(--orange-warm)"/>
    <path d="M440 100 L660 100 L660 377 L150 377 C310 335 430 270 440 178 Z" fill="var(--charcoal)"/>
    <path d="M425 160 C415 270 300 330 120 377" fill="none" stroke="var(--charcoal)" stroke-width="9"/>
    <path d="M410 150 C402 265 290 325 95 377" fill="none" stroke="var(--orange-warm)" stroke-width="6"/>
    <circle cx="440" cy="100" r="80" fill="var(--paper)"/>
    <circle cx="440" cy="100" r="74" fill="var(--orange-warm)"/>
    <path d="M0 377 L0 360 C60 368 120 372 190 366 L150 377 Z" fill="var(--orange-warm)"/>
    <circle cx="0" cy="210" r="22" fill="var(--orange-warm)"/>
  </svg>

  <h2 class="front-title">Velmora Linkway</h2>

  <div class="person">
    <p class="person-name">Marin Castell</p>
    <p class="person-role">Director</p>
  </div>

  <address class="address" style="font-style:normal">
    P.O. Box 7384<br>Grand Rapids, M I 49568
  </address>

  <ul class="contacts">
    <li>(616) 555-0142
      <svg viewBox="0 0 12 12"><path d="M2 1 L4.5 1 L5.5 3.5 L4 4.5 C4.8 6.2 5.8 7.2 7.5 8 L8.5 6.5 L11 7.5 L11 10 C6 11 1 6 2 1 Z" fill="var(--orange-warm)"/></svg>
    </li>
    <li>(616) 555-0187
      <svg viewBox="0 0 12 12"><rect x="3" y="0.5" width="6" height="11" rx="1.2" fill="none" stroke="var(--orange-warm)" stroke-width="1.3"/><circle cx="6" cy="9.5" r="0.8" fill="var(--orange-warm)"/></svg>
    </li>
    <li>info@velmoralinkway.com
      <svg viewBox="0 0 12 12"><rect x="0.7" y="2" width="10.6" height="8" rx="1" fill="none" stroke="var(--orange-warm)" stroke-width="1.3"/><path d="M1 2.5 L6 6.5 L11 2.5" fill="none" stroke="var(--orange-warm)" stroke-width="1.2"/></svg>
    </li>
    <li><span>www.<span class="accent">velmoralinkway</span>.com</span>
      <svg viewBox="0 0 12 12"><circle cx="6" cy="6" r="5.2" fill="none" stroke="var(--orange-warm)" stroke-width="1.2"/><ellipse cx="6" cy="6" rx="2.2" ry="5.2" fill="none" stroke="var(--orange-warm)" stroke-width="1"/><path d="M1 6 H11" stroke="var(--orange-warm)" stroke-width="1"/></svg>
    </li>
  </ul>
</section>

</body>
</html>
```